Bright Tooth Dentistry Business Card

We need business cards for our dental office.
We are looking for a clean, elegant design

We provide dental services to children.
Our card needs to be appealing to referring dentists, parents and our team

Target Market(s)

referring dentists, parents and our team

Industry/Entity Type

Dental Clinic

Contact Information for Business Card

4816 Juniper Lane, Suite 210
Maple Ridge, PA 15237

412-837-2961 Voice
412-837-2962 fax
info@brighttoothdentalpa.com email
www.brighttoothdentalpa.com web

Font styles to use
Sans Serif

Requirements
Must have
• White background - clean, crisp, elegant, simple
• rounded corners
• different color palate - once we come up with design, we will replace the blue with orange, green,
Nice to have
• Follow our logo typeface and colors
• then we can replace color

```html
<!DOCTYPE html>
<html lang="en">
<head>
<meta charset="utf-8">
<title>Bright Tooth Dentistry – Business Card</title>
<link href="https://fonts.googleapis.com/css2?family=Montserrat:wght@400;500;600&display=swap" rel="stylesheet">
<style>
  :root {
    --brand-blue: #1aa3e0;
    --text-grey: #6f6f73;
    --card-white: #f7f7f8;
    --stage: #e4e5e8;
  }
  * { box-sizing: border-box; margin: 0; padding: 0; }
  html, body {
    width: 1200px; height: 1021px; overflow: hidden;
    background: var(--stage);
    font-family: "Montserrat", sans-serif;
  }
  .card {
    position: absolute; left: 260px; width: 680px; height: 388px;
    background: linear-gradient(160deg, #ffffff 0%, var(--card-white) 100%);
    border-radius: 26px;
    box-shadow: 0 6px 18px rgba(0,0,0,0.12);
    overflow: hidden;
  }
  .card--front { top: 92px; }
  .card--back { top: 540px; }

  .brand {
    display: flex; align-items: center; gap: 12px;
    color: var(--brand-blue); font-weight: 600; white-space: nowrap;
  }
  .brand__dot {
    width: 14px; height: 14px; border-radius: 50%; background: var(--brand-blue);
  }
  .card--front .brand {
    position: absolute; left: 0; right: 0; top: 150px;
    justify-content: center; font-size: 40px;
  }
  .front-web {
    position: absolute; left: 0; right: 0; top: 300px; text-align: center;
    font-size: 15px; color: var(--text-grey); font-weight: 500;
  }
  .front-web strong { color: var(--brand-blue); font-weight: 600; }

  .holder { position: absolute; left: 48px; top: 118px; }
  .holder__name { color: var(--brand-blue); font-size: 24px; font-weight: 600; }
  .holder__title { color: var(--text-grey); font-size: 16px; margin-top: 2px; }

  .card--back .brand {
    position: absolute; right: 44px; top: 96px; font-size: 26px;
  }
  .contact {
    position: absolute; right: 44px; top: 178px; text-align: right;
    color: var(--text-grey); font-size: 17px; line-height: 1.32;
  }
  .contact__address { margin-bottom: 10px; }
  .contact__row { display: flex; justify-content: flex-end; align-items: center; gap: 8px; }
  .contact__row svg { width: 17px; height: 17px; flex: none; }
</style>
</head>
<body>
  <section class="card card--front">
    <div class="brand"><span class="brand__dot"></span>Bright Tooth Dentistry</div>
    <p class="front-web">www.<strong>brighttoothdentalpa</strong>.com</p>
  </section>

  <section class="card card--back">
    <div class="holder">
      <p class="holder__name">Daniel Harper</p>
      <p class="holder__title">President</p>
    </div>

    <div class="brand"><span class="brand__dot"></span>Bright Tooth Dentistry</div>

    <div class="contact">
      <p class="contact__address">4816 Juniper Lane, Suite 210<br>Maple Ridge, PA 15237</p>
      <p class="contact__row">412-837-2961
        <svg viewBox="0 0 24 24" aria-hidden="true"><path fill="#1aa3e0" d="M6.6 10.8a15.2 15.2 0 0 0 6.6 6.6l2.2-2.2a1 1 0 0 1 1-.25 11.4 11.4 0 0 0 3.6.57 1 1 0 0 1 1 1V20a1 1 0 0 1-1 1A17 17 0 0 1 3 4a1 1 0 0 1 1-1h3.5a1 1 0 0 1 1 1c0 1.25.2 2.45.57 3.6a1 1 0 0 1-.25 1z"/></svg>
      </p>
      <p class="contact__row">412-837-2962
        <svg viewBox="0 0 24 24" aria-hidden="true"><path fill="#1aa3e0" d="M7 3h10v4H7zM4 8h16a2 2 0 0 1 2 2v6h-4v5H6v-5H2v-6a2 2 0 0 1 2-2zm4 8v3h8v-3z"/></svg>
      </p>
      <p class="contact__row">info@brighttoothdentalpa.com
        <svg viewBox="0 0 24 24" aria-hidden="true"><rect x="2.5" y="5" width="19" height="14" rx="1.5" fill="none" stroke="#1aa3e0" stroke-width="2"/><path d="M3 6l9 7 9-7" fill="none" stroke="#1aa3e0" stroke-width="2"/></svg>
      </p>
      <p class="contact__row">www.brighttoothdentalpa.com
        <svg viewBox="0 0 24 24" aria-hidden="true"><g fill="none" stroke="#1aa3e0" stroke-width="1.8"><circle cx="12" cy="12" r="9.5"/><ellipse cx="12" cy="12" rx="4" ry="9.5"/><path d="M2.5 12h19M4 7h16M4 17h16"/></g></svg>
      </p>
    </div>
  </section>
</body>
</html>
```